依頼詳細
以下の4つのデザインをお願いいたします。

①社会保険労務士事務所の事務所案内パンフレット(縦型A4仕上がり折りパンフレット・カラー4P)
②社会保険労務士の料金表・スタッフ紹介(縦型A4両面・カラー2P)
③税理士事務所の事務所案内パンフレット(縦型A4仕上がり折りパンフレット・カラー4P)
④税理士事務所の料金表・スタッフ紹介(縦型A4両面・カラー2P)

税理士と社会保険労務士は、デザインは、ほぼ同じで色違いで作成ください。
(税理士=青系、社会保険労務士=緑系)

事務所案内パンフレットの外側(表面・裏面)は、桐谷公園をイメージしたデザインでお願いします。

事務所の地図の資料をアップしますので、わかり易い地図をご作成ください。

代表者挨拶のT&Rとは?の部分は、うまくデザインいただくと嬉しいです。

納品は、「イラストレーター形式のもの」と「PDF化したもの」をお願いします。

その他、ご不明な点がありましたら、コメントください。

サイズ
A4
ページ数
12ページ
希望イメージ
シンプル 複雑
単色 カラフル
暗い 明るい
日常 高級
遊び心 厳粛
未来的 伝統的
女性的 男性的
希望する色
青系、緑系
納品ファイル
• イラストレーター形式 (.ai)
補足説明
代表者の写真は、一応複数アップいたします。
必要に合わせて、使ってください。
社会保険労務士事務所の案内パンフレットの資料をアップします。

※サービス内容は、内側の左と右に使ってください。

社会保険労務士事務所の料金表とスタッフ紹介をアップします。
税理士事務所の案内パンフレットの資料をアップしました。

※社会保険労務士事務所と違う部分は、赤字にしてあります。

税理士事務所の料金表とスタッフ紹介の資料をアップしました。

※スタッフ案内の方も、社会保険労務士事務所と若干文言を変えています。
縦型A4仕上がり折りパンフレットの方は、A4の原稿をつなげたA3で納品お願いします。

料金表・スタッフ紹介(縦型A4両面・カラー2P)の方は、A4で2枚に作成でお願いします。
日数を延期させていただきました。
宜しくお願いいたします。
締切を延長いたしました。
たくさんご提案いただき、ありがとうございます。

申し訳ないのですが、なかなかピンとくるご提案がなく、選びかねております。

私のご依頼の仕方が、まずかったかもしれません。

パンフレット表紙については、「桐谷公園をイメージしたデザイン」と書いたので、あまりにも、そちらによってしまったみたいです。

デザイン的に、そういったもの(海とか、公園とか、緑の木々)を想起させるという感じだったのですが…。

写真がいけない訳ではないのですが、あまりにも、桐谷公園が全面にでてしまい、士業の事務所っぽくなくなってしまっているようです。

あまり、桐谷公園を意識しすぎず、士業のパンフレットっぽく修正いただけると嬉しいです。

また、パンフレット内側については、代表者挨拶が左側全面になっているのですが、サービス内容の一部を左側にもってきていただき、代表者挨拶とT&Rの部分は、少し小さ目にしていただけると助かります。あくまでも、サービスの内容がメインになります。

あと、スタッフ紹介の私のところについては、T&Rブログの紹介は無しでお願いします。

日程を、もう一度だけ、延長させていただきました。

お手数をお掛けしますが、宜しくおねがいいたします。
■ 選んだ理由

PX-RWさんの提案は、サービス案内やスタッフ紹介などについても、デザインに工夫があり、全体のバランスも、士業向けにしっかりしたものになっていたので、選ばせていただきました。
素晴らしいご提案ありがとうございました!

■ 提案者全員のお礼・コメント

たくさんの皆さんに、ご提案をいただきありがとうございました。
追加でご提案いただいた作品のなかには、迷う作品もありました。
今後とも、宜しくお願いいたします。

```html
<!DOCTYPE html>
<html lang="ja">
<head>
<meta charset="utf-8">
<title>T&amp;R 税理士事務所 事務所案内</title>
<link rel="stylesheet" href="https://fonts.googleapis.com/css2?family=Noto+Sans+JP:wght@700&family=Cormorant+Garamond:wght@500&display=swap">
<style>
  :root {
    --band: #a9d5f0;
    --band-deep: #8cc4e8;
    --title-blue: #1d8ed6;
    --brand-navy: #1f3f8f;
    --paper: #ffffff;
    --sky-top: #ffffff;
    --sky-mid: #cfe6f6;
    --sky-low: #9ccbea;
    --tree-light: #6fa33c;
    --tree-dark: #2f5a1e;
  }
  * { margin: 0; padding: 0; box-sizing: border-box; }
  html, body { width: 848px; height: 1200px; overflow: hidden; background: var(--paper); }
  .cover {
    position: relative;
    width: 848px;
    height: 1200px;
    background: var(--paper);
    overflow: hidden;
  }
  .top-band {
    position: absolute; left: 0; top: 0;
    width: 100%; height: 16px;
    background: var(--band);
  }
  .park-visual {
    position: absolute; left: 0; top: 330px;
    width: 100%; height: 800px;
    background:
      linear-gradient(180deg,
        rgba(255,255,255,1) 0%,
        rgba(255,255,255,0) 22%),
      linear-gradient(180deg,
        var(--sky-top) 0%,
        var(--sky-mid) 30%,
        var(--sky-low) 52%,
        var(--tree-light) 66%,
        var(--tree-dark) 84%,
        #4c7a2e 100%);
  }
  .brand {
    position: absolute; top: 62px; left: 0; width: 100%;
    display: flex; flex-direction: column; align-items: center; gap: 14px;
  }
  .brand-square {
    width: 64px; height: 64px;
    background: var(--brand-navy);
  }
  .brand-name {
    font-family: "Cormorant Garamond", serif;
    font-weight: 500;
    font-size: 22px;
    color: var(--brand-navy);
    letter-spacing: 0.02em;
  }
  .office-title {
    position: absolute; top: 258px; left: 0; width: 100%;
    text-align: center;
    font-family: "Noto Sans JP", sans-serif;
    font-weight: 700;
    font-size: 38px;
    letter-spacing: 0.06em;
    color: var(--title-blue);
  }
  .motto {
    position: absolute; top: 985px; left: 0; width: 100%;
    text-align: center;
    font-family: "Cormorant Garamond", serif;
    font-weight: 500;
    font-size: 88px;
    color: #ffffff;
    letter-spacing: 0.01em;
    text-shadow: 0 2px 6px rgba(0,0,0,0.25);
  }
  .bottom-band {
    position: absolute; left: 0; bottom: 0;
    width: 100%; height: 70px;
    background: var(--band);
    border-top: 6px solid var(--paper);
  }
</style>
</head>
<body>
<main class="cover">
  <div class="top-band"></div>
  <div class="park-visual" role="img" aria-label="桐谷公園の写真：青空にそびえる展望塔と緑の木々、花壇と街灯のある公園"></div>
  <header class="brand">
    <div class="brand-square"></div>
    <span class="brand-name">Trust &amp; Reason</span>
  </header>
  <h1 class="office-title">T&amp;R 税理士事務所</h1>
  <p class="motto">Trust &amp; Reason</p>
  <div class="bottom-band"></div>
</main>
</body>
</html>
```